Qarnetix EIRL Business Card Design Project

We need a business card design for a New Business Intelligence Consultant. We bring a complete service to the client from first consulting meeting to help desk and system improvement.

I will upload the company logo and I like to use the logo colors on the card. Feel free to use all logo components on the design, for example one side with the black logo using complete card and the other side only the red shape (is an example, feel absolutely free :)).

The principal idea is to sell a professional service and a modern company.

Target Market(s)

IT Business Intelligence Clients

Industry/Entity Type

Professional Service

Requirements
Nice to have
• - Use the logo colors and minimize white sections.
- Rounded borders
Should not have
• I don't want to see any references to people working on a meeting or office photos or any computers related logos.

```html
<!DOCTYPE html>
<html lang="es">
<head>
<meta charset="utf-8">
<title>Qarnetix EIRL – Tarjeta de presentación</title>
<link rel="stylesheet" href="https://fonts.googleapis.com/css2?family=Arimo:wght@400;700&display=swap">
<style>
  :root {
    --stage: #1c1c1e;
    --card: #0b0b0c;
    --red: #e8262c;
    --grey: #a7a8aa;
    --grey-light: #c9cacc;
    --white: #f2f2f2;
  }
  * { box-sizing: border-box; margin: 0; padding: 0; }
  html, body { width: 1200px; height: 984px; overflow: hidden; }
  body {
    background: var(--stage);
    font-family: "Arimo", Arial, sans-serif;
    position: relative;
  }
  .card {
    position: absolute;
    left: 250px;
    width: 700px;
    height: 400px;
    background: var(--card);
    border-radius: 16px;
    overflow: hidden;
    box-shadow: 0 10px 30px rgba(0,0,0,.5);
  }
  .card--back { top: 62px; }
  .card--front { top: 522px; }

  /* back side */
  .brand-small {
    position: absolute; left: 44px; top: 46px;
    display: flex; align-items: center; gap: 12px;
  }
  .brand-small__square { width: 26px; height: 26px; background: var(--red); }
  .brand-small__name { color: var(--red); font-weight: 700; font-size: 34px; letter-spacing: .5px; }

  .band-accent { position: absolute; inset: 0; }
  .title {
    position: absolute; right: 44px; top: 136px;
    color: #333; font-size: 15px;
    background: var(--grey-light); padding: 3px 10px 3px 8px;
  }
  .name {
    position: absolute; left: 48px; top: 176px;
    color: var(--red); font-weight: 700; font-size: 26px; letter-spacing: 2.5px;
  }
  .company {
    position: absolute; left: 48px; top: 262px;
    color: var(--grey); font-size: 16px; line-height: 1.45;
  }
  .company strong { color: var(--white); }
  .contacts {
    position: absolute; left: 410px; top: 254px;
    list-style: none; color: var(--grey); font-size: 16px;
  }
  .contacts li { display: flex; align-items: center; gap: 14px; height: 27px; }
  .contacts svg { width: 16px; height: 16px; flex: none; }

  /* front side */
  .brand-large {
    position: absolute; right: 58px; top: 196px;
    display: flex; align-items: center; gap: 20px;
  }
  .brand-large__square { width: 52px; height: 52px; background: var(--red); }
  .brand-large__name { color: var(--grey-light); font-weight: 400; font-size: 82px; letter-spacing: 1px; }
  .front-rule {
    position: absolute; right: 40px; top: 300px;
    width: 400px; height: 2px;
    background: linear-gradient(90deg, transparent, var(--grey) 35%, var(--grey));
  }
  .front-url {
    position: absolute; right: 60px; top: 316px;
    color: var(--grey); font-size: 20px; letter-spacing: 5px;
  }
</style>
</head>
<body>
  <section class="card card--back" aria-label="Reverso de la tarjeta">
    <svg class="band-accent" width="700" height="400" viewBox="0 0 700 400" aria-hidden="true">
      <polygon points="430,130 700,118 700,150 400,160" fill="#8d8e90"/>
      <polygon points="0,165 700,150 700,200 0,215" fill="var(--grey-light)"/>
      <polygon points="0,218 700,203 700,209 0,224" fill="var(--red)"/>
    </svg>
    <div class="brand-small">
      <span class="brand-small__square"></span>
      <span class="brand-small__name">qarnetix</span>
    </div>
    <p class="title">| Gerente General</p>
    <p class="name">TOMÁS FUENTES A.</p>
    <p class="company"><strong>Qarnetix EIRL</strong><br>Av. Los Robles 1450<br>Of. 302, Santiago</p>
    <ul class="contacts">
      <li><svg viewBox="0 0 16 16"><rect x="2" y="2" width="12" height="12" rx="2" fill="var(--red)"/><rect x="5" y="4" width="6" height="3" fill="var(--card)"/></svg>+56 (9) 81264305</li>
      <li><svg viewBox="0 0 16 16"><rect x="1" y="3" width="14" height="10" rx="2" fill="var(--red)"/><polyline points="2,4 8,9 14,4" fill="none" stroke="var(--card)" stroke-width="1.5"/></svg>tomas@qarnetix.cl</li>
      <li><svg viewBox="0 0 16 16"><circle cx="8" cy="8" r="7" fill="var(--red)"/><path d="M1 8h14M8 1c-3 4-3 10 0 14M8 1c3 4 3 10 0 14" fill="none" stroke="var(--card)" stroke-width="1.2"/></svg>www.qarnetix.cl</li>
    </ul>
  </section>

  <section class="card card--front" aria-label="Anverso de la tarjeta">
    <div class="brand-large">
      <span class="brand-large__square"></span>
      <span class="brand-large__name">qarnetix</span>
    </div>
    <div class="front-rule"></div>
    <p class="front-url">www.qarnetix.cl</p>
  </section>
</body>
</html>
```